Report Design

I am looking for a redesign of our monthly inspection reports we submit to our customers. I uploaded the current one we use (FernHollow) and also that of a competitor (Calm Ridge). I want to more copy the layout of the Calmridge report I attached but with more flow and design.

Requirements
Must have
• This has to be in a template format that we can modify the content every month.

```html
<!DOCTYPE html>
<html lang="en">
<head>
<meta charset="utf-8">
<title>Landscape, Irr. &amp; Property Inspection – Report 1</title>
<link href="https://fonts.googleapis.com/css2?family=Signika:wght@400;600;700&family=Mada:wght@400;500&display=swap" rel="stylesheet">
<style>
  :root {
    --green-dark: #006a35;
    --green-light: #55c34a;
    --green-text: #0b6b35;
    --ink: #111111;
    --body: #222222;
    --paper: #ffffff;
  }
  html, body { margin: 0; padding: 0; overflow: hidden; background: var(--paper); }
  .page {
    position: relative; width: 848px; height: 1200px; overflow: hidden;
    background: var(--paper); font-family: "Mada", sans-serif; color: var(--body);
  }
  .report-title {
    position: absolute; left: 49px; top: 52px; margin: 0;
    font-family: "Signika", sans-serif; font-weight: 700; font-size: 24px; color: var(--ink);
  }
  .property-band {
    position: absolute; left: 50px; top: 94px; width: 691px; height: 54px;
    background: var(--green-dark); color: #fff;
    font-family: "Signika", sans-serif; font-weight: 700; font-size: 25px;
    display: flex; align-items: center; padding-left: 13px; box-sizing: border-box;
  }
  .page-number {
    position: absolute; left: 757px; top: 94px; width: 51px; height: 54px;
    background: var(--green-light); color: #fff;
    font-family: "Signika", sans-serif; font-weight: 700; font-size: 25px;
    display: flex; align-items: center; justify-content: center;
  }
  .section {
    position: absolute; left: 50px; width: 756px; box-sizing: border-box;
    border: 1.5px solid var(--green-dark);
  }
  .section-grasses { top: 170px; height: 427px; }
  .section-flowers { top: 616px; height: 444px; }
  .section-heading {
    position: absolute; left: 22px; margin: 0;
    font-family: "Signika", sans-serif; font-weight: 600; font-size: 18px; color: var(--green-text);
  }
  .section-text {
    position: absolute; left: 22px; right: 18px; margin: 0;
    font-size: 15.4px; line-height: 19px; color: var(--body);
  }
  .photo { position: absolute; width: 340px; height: 292px; }
  .photo-grass-bed { background: linear-gradient(180deg, #dcdad2 0%, #c9c5b8 45%, #6f6c66 100%); }
  .photo-muhly { background: linear-gradient(180deg, #eef0f2 0%, #c8a9b4 45%, #5f8a3c 75%, #58903a 100%); }
  .photo-entrance { background: linear-gradient(180deg, #e7eaee 0%, #7d7f76 35%, #5d5f63 60%, #4f6e34 100%); }
  .footer-rule {
    position: absolute; left: 50px; top: 1085px; width: 759px; height: 1.5px; background: var(--green-dark);
  }
  .footer-title {
    position: absolute; left: 61px; top: 1102px; margin: 0;
    font-family: "Signika", sans-serif; font-weight: 700; font-size: 20px; color: var(--ink);
  }
  .footer-division {
    position: absolute; left: 62px; top: 1132px; margin: 0; font-size: 16px; color: var(--green-text);
  }
  .footer-contacts {
    position: absolute; left: 62px; top: 1160px; display: flex; gap: 26px;
    font-size: 14.5px; color: var(--body);
  }
  .contact { display: flex; align-items: center; gap: 7px; }
  .contact svg { width: 14px; height: 14px; }
  .brand {
    position: absolute; left: 664px; top: 1128px; width: 148px; text-align: center;
  }
  .brand-mark { width: 16px; height: 16px; background: var(--green-dark); margin: 0 auto 4px; }
  .brand-name {
    font-family: "Signika", sans-serif; font-weight: 700; font-size: 23px; color: var(--ink); line-height: 1;
  }
  .brand-tag { font-family: "Signika", sans-serif; font-size: 9.5px; color: var(--ink); margin-top: 3px; }
</style>
</head>
<body>
<div class="page">
  <h1 class="report-title">Landscape, Irr. &amp; Property Inspection</h1>
  <div class="property-band">Gardens on Westbrook POA &amp; Retail</div>
  <div class="page-number">1</div>

  <section class="section section-grasses">
    <h2 class="section-heading" style="top:26px">1. Grasses Throughout</h2>
    <p class="section-text" style="top:54px">Right now, the Muhly grass is blooming and looks great. The crew went around and trimmed them all up so they look fresh and clean. There were some of the types that were not blooming, that we trimmed back farther.</p>
    <div class="photo photo-grass-bed" style="left:22px; top:104px" role="img" aria-label="Trimmed ornamental grasses in a mulched bed along a building wall and curb"></div>
    <div class="photo photo-muhly" style="left:390px; top:104px" role="img" aria-label="Blooming pink Muhly grass bed beside lawn and curb"></div>
  </section>

  <section class="section section-flowers">
    <h2 class="section-heading" style="top:24px">2.&nbsp;&nbsp; Flowers:</h2>
    <p class="section-text" style="top:54px">Both main entrances are in need of fresh flowers.</p>
    <div class="photo photo-entrance" style="left:22px; top:120px" role="img" aria-label="Main entrance median bed with mulch and no flowers, street and apartments behind"></div>
  </section>

  <div class="footer-rule"></div>
  <h2 class="footer-title">Landscape, Irr. &amp; Property Inspection</h2>
  <p class="footer-division">Landscape and Grounds Maintenance Division</p>
  <div class="footer-contacts">
    <span class="contact">
      <svg viewBox="0 0 16 16"><circle cx="8" cy="8" r="8" fill="#111"/><path d="M5 4.5l1.5-.5 1 2-1 1c.5 1 1.3 1.8 2.3 2.3l1-1 2 1-.5 1.5C9 11 5 7 5 4.5z" fill="#fff"/></svg>
      352-555-0142</span>
    <span class="contact">
      <svg viewBox="0 0 16 16"><circle cx="8" cy="8" r="8" fill="#111"/><rect x="4.5" y="6.5" width="7" height="4.5" fill="#fff"/><rect x="5.5" y="4.5" width="5" height="2" fill="#fff"/></svg>
      Fax 877-555-0187</span>
    <span class="contact">
      <svg viewBox="0 0 16 16"><circle cx="8" cy="8" r="8" fill="#111"/><path d="M8 3.5a3 3 0 0 1 3 3c0 2.2-3 5.5-3 5.5S5 8.7 5 6.5a3 3 0 0 1 3-3z" fill="#fff"/><circle cx="8" cy="6.5" r="1.1" fill="#111"/></svg>
      1420 Larkspur Road, Pine Hollow, FL 33599</span>
  </div>

  <div class="brand">
    <div class="brand-mark"></div>
    <div class="brand-name">FernHollow</div>
    <div class="brand-tag">Landscape and Maintenance, Inc.</div>
  </div>
</div>
</body>
</html>
```